Top header for website

Header for website Size is 1000px x 120px
I have CS5 so will need the source files photoshop, illustrator etc, so I can change text and photos.
Photos attached, includes example header and screenshot of eg site
Brief:
I need a website header for golfers where I can change the photos and their name.
The header needs to have these things.
- pictures of the golfer (use from pics attached)
- Their name
- Also under there name is smaller text I need a line of text you can just say "Offical Website" in your e.g to me
so for example you should have
Dale Fenwick
Offical Website
And some photos that are blended with some nice golf background or some grass or other ideas that you come up with that will look better than mine I'm sure :)
Size is 1000px x 120px
It needs to look professional and blend in nicely. I don't mind how many photos are used maybe 1-4?
The text needs to look professional too but not boring.
The header you create will be used on a website for a Professional Golfer (tour pro) their job is golf, their website needs to showcase them and promote them as best as possible.
As I said above I will need to swap photos easily and edit the text so will need the source files.
So a important point here. I guess there is no need to blend or do anything to the photos you add as I will actually need to change the photos and just need a simple template that I can swap photos and edit their name.
Ultimately I would like 3 versions of the header done and source files for all 3 so I can give them(the golfers) a choice of header type.
See how you go.
Remember that the header must have the ability for me to easily swap images and of course change the text.
My goal is to use the same header for each golfer but obviously with their images and their name.
I have CS5 so will need the source files photoshop, illustrator etc
2 example headers are attached to show you my attempts :) Please do something better.
I don't want any flash.

```html
<!DOCTYPE html>
<html lang="en">
<head>
<meta charset="utf-8">
<title>Dale Fenwick – Official Website Header</title>
<link rel="stylesheet" href="https://fonts.googleapis.com/css2?family=Open+Sans:wght@300;400;700;800&display=swap">
<style>
  :root {
    --bg-light: #f2f2f2;
    --bg-mid: #d4d4d4;
    --band-dark: #0f3a0c;
    --band-deep: #1d5a14;
    --band-bright: #5cc236;
    --band-glow: #a8e67e;
    --frame: #2f4a2a;
    --frame-inner: #6f8a66;
    --name: #ffffff;
    --tagline: #1c1c1c;
  }
  html, body {
    margin: 0;
    padding: 0;
    width: 1200px;
    height: 144px;
    overflow: hidden;
    background: var(--bg-light);
  }
  .site-header {
    position: relative;
    width: 1200px;
    height: 144px;
    overflow: hidden;
    background: linear-gradient(180deg, var(--bg-light) 0%, #e6e6e6 22%, var(--bg-light) 70%, var(--bg-mid) 100%);
    font-family: "Open Sans", Arial, sans-serif;
  }
  .brand-band {
    position: absolute;
    left: 0;
    top: 36px;
    width: 1200px;
    height: 68px;
    background: linear-gradient(180deg,
      var(--band-glow) 0%,
      var(--band-bright) 10%,
      var(--band-deep) 22%,
      var(--band-dark) 45%,
      var(--band-dark) 72%,
      var(--band-deep) 84%,
      var(--band-bright) 94%,
      var(--band-glow) 100%);
    box-shadow: 0 2px 4px rgba(0,0,0,0.25);
  }
  .golfer-name {
    position: absolute;
    left: 40px;
    top: 34px;
    margin: 0;
    font-size: 60px;
    line-height: 72px;
    letter-spacing: -1px;
    color: var(--name);
    text-transform: uppercase;
    text-shadow: 0 2px 3px rgba(0,0,0,0.45);
    white-space: nowrap;
  }
  .golfer-name .first { font-weight: 300; }
  .golfer-name .last { font-weight: 700; }
  .tagline {
    position: absolute;
    left: 200px;
    top: 107px;
    margin: 0;
    font-size: 13px;
    font-weight: 700;
    letter-spacing: 0.6px;
    color: var(--tagline);
  }
  .photo-strip {
    position: absolute;
    left: 564px;
    top: 9px;
    display: flex;
    gap: 20px;
  }
  .photo-frame {
    width: 190px;
    height: 120px;
    border-radius: 6px;
    border: 2px solid var(--frame);
    box-shadow: inset 0 0 0 1px var(--frame-inner), 0 2px 5px rgba(0,0,0,0.45);
    box-sizing: border-box;
    overflow: hidden;
  }
  .photo-portrait { background: linear-gradient(160deg, #6e7c3c 0%, #a89a72 45%, #c9a88a 70%, #e8e8e4 100%); }
  .photo-swing { background: linear-gradient(180deg, #3f5a2a 0%, #6b7d4c 45%, #d8d8d4 75%, #f0f0f0 100%); }
  .photo-bunker { background: linear-gradient(200deg, #2f4a1e 0%, #4f7a2c 40%, #8a9a5a 70%, #c7b78e 100%); }
</style>
</head>
<body>
  <header class="site-header">
    <div class="brand-band"></div>
    <h1 class="golfer-name"><span class="first">Dale</span><span class="last">Fenwick</span></h1>
    <p class="tagline">Offical Website</p>
    <div class="photo-strip">
      <div class="photo-frame photo-portrait" role="img" aria-label="Close-up photo of the golfer wearing a white cap"></div>
      <div class="photo-frame photo-swing" role="img" aria-label="Photo of the golfer finishing a tee shot at a tournament"></div>
      <div class="photo-frame photo-bunker" role="img" aria-label="Photo of the golfer playing a shot from a greenside bunker"></div>
    </div>
  </header>
</body>
</html>
```